The Corvane Agency

We are a pr, social media and strategy agency specializing in the pet industry. We would like a new dynamic design of our existing website. We think it is currently outdated and looks too corporate. We would like it to look more consumer oriented as we primarily market pet products. We would like warm imagery involving pets and while pets are fun, this is still a business website and needs to maintain a professional look. We are hired by business owners and executives.
I would like some of our work featured on the home page.
Our primary service tabs are:
Public Relations
Social Media
Product Consulting
Most of the content will remain the same but we are open to suggestions!
Our current website can be found at www.corvanepetpr.example.
We are open to other colors than in our logo and on our current page.
This is a design only project and will not require programming. The selected designer will need to provide at least one interior page in addition to the home page.

Industry/Entity Type

Pet

Requirements
Should not have
• Cartoon type figures. Pet puns.

```html
<!DOCTYPE html>
<html lang="en">
<head>
<meta charset="utf-8">
<title>The Corvane Agency — Pet PR, Social Media and Strategy</title>
<link rel="stylesheet" href="https://fonts.googleapis.com/css2?family=Ubuntu:wght@400;500;700&family=Open+Sans:wght@400;600&display=swap">
<style>
  :root{
    --page:#f2f1ef;
    --white:#ffffff;
    --orange:#f57c1f;
    --orange-title:#e8701a;
    --rust:#b3340f;
    --red-line:#c8411f;
    --brand-red:#d81f35;
    --blue:#1aa3e8;
    --text:#555555;
    --dark-text:#3a2a20;
    --footer:#1f2329;
    --footer-text:#a9adb3;
    --parchment-a:#e6d7ba;
    --parchment-b:#f5efe2;
  }
  *{box-sizing:border-box;margin:0;padding:0}
  html,body{width:780px;height:1200px;overflow:hidden}
  body{background:var(--page);font-family:"Open Sans",sans-serif;color:var(--text);position:relative}
  .abs{position:absolute}

  /* header */
  .topline{left:0;top:0;width:780px;height:3px;background:var(--blue)}
  .header{left:0;top:3px;width:780px;height:83px;background:var(--page)}
  .brand{left:108px;top:27px;display:flex;align-items:center;gap:6px}
  .brand-dot{width:7px;height:7px;border-radius:50%;background:var(--brand-red)}
  .brand-name{font-family:"Ubuntu",sans-serif;font-weight:500;font-size:18px;color:var(--brand-red)}
  .nav{left:337px;top:24px;display:flex;align-items:center;height:36px}
  .nav a{font-family:"Ubuntu",sans-serif;font-size:8.4px;color:#333;text-decoration:none;padding:0 6px;line-height:36px;text-transform:uppercase}
  .nav a.active{background:var(--orange);color:#fff;padding:0 11px}

  /* hero */
  .hero{left:0;top:86px;width:780px;height:219px;background:linear-gradient(90deg,var(--parchment-a),#efe4cf 55%,var(--parchment-b));border-bottom:1.5px solid var(--red-line)}
  .hero-photo{left:440px;top:86px;width:200px;height:218px;
    background:
      linear-gradient(180deg,rgba(40,26,16,.55) 0%,rgba(40,26,16,0) 45%,rgba(150,90,45,.35) 100%),
      linear-gradient(90deg,#cdb48f 0%,#7a5232 14%,#4a3220 38%,#5a3b24 62%,#8a5a32 86%,#d7c3a0 100%)}
  .hero-title{left:108px;top:120px;font-family:"Ubuntu",sans-serif;font-weight:700;font-size:27px;line-height:32px;color:var(--rust)}
  .hero-sub{left:108px;top:198px;font-family:"Ubuntu",sans-serif;font-weight:400;font-size:21px;line-height:26px;color:var(--dark-text)}
  .hero-sub b{font-weight:500}

  /* service cards */
  .card{top:355px;width:180px;height:233px;background:var(--white);border-bottom:2px solid var(--orange);text-align:center}
  .card-image{position:absolute;top:26px;height:90px}
  .card h3{position:absolute;left:0;right:0;top:129px;font-family:"Ubuntu",sans-serif;font-weight:400;font-size:12.6px;color:var(--orange-title)}
  .card p{position:absolute;left:14px;right:14px;top:155px;font-size:7.8px;line-height:13px}
  .read-more{font-size:7.8px;color:var(--blue)}
  .card .read-more{position:absolute;left:0;right:0;top:206px}

  /* services & testimonial */
  .section-title{top:623px;font-family:"Ubuntu",sans-serif;font-weight:400;font-size:16.5px;color:var(--orange-title)}
  .service-box{left:108px;top:655px;width:277px;height:111px;background:var(--white)}
  .service-photo{position:absolute;left:1px;top:14px;width:110px;height:80px;
    background:linear-gradient(90deg,#f4e6cc 0%,#dcb57a 30%,#c9974f 55%,#e2c08a 80%,#fbf5ea 100%)}
  .service-box p{position:absolute;left:126px;top:21px;width:142px;font-size:8.6px;line-height:13px}
  .service-box .read-more{position:absolute;left:126px;top:87px}
  .quote-box{left:396px;top:655px;width:276px;height:111px;background:var(--white);border-left:2px solid var(--blue)}
  .quote-mark{position:absolute;left:14px;top:30px}
  .quote-box p{position:absolute;left:76px;top:27px;width:190px;font-size:8.8px;line-height:13.5px}
  .quote-author{position:absolute;left:76px;top:67px;font-size:7.2px;color:var(--blue)}
  .slider-btn{top:637px;width:18px;height:17px;display:flex;align-items:center;justify-content:center}
  .slider-btn.prev{left:636px;background:#e4e4e4}
  .slider-btn.next{left:654px;background:var(--blue)}

  /* banner */
  .banner{left:108px;top:811px;width:564px;height:133px;background:linear-gradient(90deg,#d8c8a8,#efe5d2 55%,#e8dcc4);border-bottom:2px solid var(--red-line)}
  .banner-photo{position:absolute;left:384px;top:0;width:100px;height:131px;
    background:linear-gradient(90deg,#e6d6ba 0%,#cf8a4c 22%,#b8602a 50%,#cf8248 78%,#e8dcc4 100%)}
  .banner h2{position:absolute;left:30px;top:20px;font-family:"Ubuntu",sans-serif;font-weight:700;font-size:17px;color:var(--rust)}
  .banner p{position:absolute;left:30px;top:52px;width:270px;font-size:10.2px;line-height:13.5px;color:var(--dark-text)}

  /* footer */
  .footer{left:0;top:991px;width:780px;height:209px;background:var(--footer)}
  .footer-title{top:1019px;font-family:"Ubuntu",sans-serif;font-weight:400;font-size:8.4px;color:var(--orange);text-transform:uppercase}
  .quick-links{left:109px;top:1045px;list-style:none}
  .quick-links li{font-size:7.8px;line-height:15.2px;color:var(--footer-text)}
  .testimonial{left:197px;width:170px;display:flex;gap:10px}
  .avatar{width:28px;height:28px;border-radius:50%;background:linear-gradient(#8b6a55,#5b4434);border:2px solid #e0e0e0;flex:none}
  .footer-copy{font-size:7px;line-height:9.5px;color:var(--footer-text)}
  .footer-copy i{display:block;margin-top:6px;color:#d8d8d8;font-size:6.8px}
  .footer-arrows{left:333px;top:1142px;display:flex;gap:4px}
  .footer-arrows span{width:12px;height:11px;background:#000;display:flex;align-items:center;justify-content:center}
  .blog-item{left:403px;width:140px}
  .view-more{left:404px;top:1144px;font-size:7.8px;color:#e0e0e0;text-decoration:underline}
  .address{left:571px;top:1046px;width:110px}
  .contact-line{left:571px;display:flex;align-items:center;gap:6px;font-size:7.4px;color:#d8d8d8}
  .social{left:573px;top:1150px;display:flex;gap:4px}
  .social span{width:18px;height:18px;border-radius:50%;background:#fff}
</style>
</head>
<body>
  <div class="abs topline"></div>
  <header class="abs header"></header>
  <div class="abs brand"><span class="brand-dot"></span><span class="brand-name">The Corvane Agency</span></div>
  <nav class="abs nav">
    <a class="active" href="#">Pet Experts</a>
    <a href="#">Business Development</a>
    <a href="#">Studies</a>
    <a href="#">Our Team</a>
    <a href="#">Case</a>
    <a href="#">PR</a>
  </nav>

  <section class="abs hero"></section>
  <div class="abs hero-photo" role="img" aria-label="Photo of a German shepherd dog with its tongue out"></div>
  <h1 class="abs hero-title">LOREM IPSUM<br>DOLOR SIT</h1>
  <p class="abs hero-sub">lorem ipsume dolor site<br><b>lorem ipsume</b> dolor sit<br>dummy text</p>

  <article class="abs card" style="left:108px">
    <div class="card-image" style="left:50px;width:92px;background:linear-gradient(180deg,#f6ede0 0%,#e2b98a 40%,#c8905e 75%,#3a2c26 100%)" role="img" aria-label="Photo of a smiling support agent wearing a headset"></div>
    <h3>PUBLIC RELATIONS</h3>
    <p>Lorem Ipsum is simply dummy text of the printing and typesetting industry. Lorem Ipsum has been the industry's</p>
    <span class="read-more">[ Read More ]</span>
  </article>
  <article class="abs card" style="left:300px">
    <div class="card-image" style="left:34px;width:116px;background:linear-gradient(180deg,#ffffff 0%,#d5ebf5 35%,#7fc3e0 70%,#ffffff 100%)" role="img" aria-label="Illustration of a tree with birds and social media bubbles"></div>
    <h3>SOCIAL MEDIA</h3>
    <p>Lorem Ipsum is simply dummy text of the printing and typesetting industry. Lorem Ipsum has been the industry's</p>
    <span class="read-more">[ Read More ]</span>
  </article>
  <article class="abs card" style="left:492px">
    <div class="card-image" style="left:65px;width:48px;top:28px;height:88px;background:linear-gradient(180deg,#e6ebe8 0%,#a9bdb6 45%,#5f7f7a 100%)" role="img" aria-label="Photo of a bag of pet food"></div>
    <h3>PRODUCT CONSULTING</h3>
    <p>Lorem Ipsum is simply dummy text of the printing and typesetting industry. Lorem Ipsum has been the industry's</p>
    <span class="read-more">[ Read More ]</span>
  </article>

  <h2 class="abs section-title" style="left:108px">OUR SERVICES</h2>
  <h2 class="abs section-title" style="left:396px">CLIENT SAY</h2>
  <div class="abs slider-btn prev"><svg width="6" height="9" viewBox="0 0 6 9"><path d="M5 1 1.5 4.5 5 8" fill="none" stroke="#bbb" stroke-width="1.2"/></svg></div>
  <div class="abs slider-btn next"><svg width="6" height="9" viewBox="0 0 6 9"><path d="M1 1 4.5 4.5 1 8" fill="none" stroke="#fff" stroke-width="1.2"/></svg></div>

  <div class="abs service-box">
    <div class="service-photo" role="img" aria-label="Photo of a golden retriever lying down"></div>
    <p>Lorem Ipsum is simply dummy text of the printing and type-setting industry. Lorem Ipsum has been the industry's...</p>
    <span class="read-more">[ Read More ]</span>
  </div>
  <div class="abs quote-box">
    <svg class="quote-mark" width="42" height="32" viewBox="0 0 42 32"><path d="M0 32V16C0 6 5 1 14 0v6c-4 1-6 4-6 8h6v18zM24 32V16C24 6 29 1 38 0v6c-4 1-6 4-6 8h6v18z" fill="#d9d9d9"/></svg>
    <p>Lorem Ipsum is simply dummy text of the printing and typesetting industry.</p>
    <span class="quote-author">Mr. Lorem ipsum</span>
  </div>

  <section class="abs banner">
    <div class="banner-photo" role="img" aria-label="Photo of a cocker spaniel"></div>
    <h2>LOREM IPSUM IS SIMPLY DUMMY</h2>
    <p>Lorem Ipsum is simply dummy text of the printing and typesetting industry. Lorem Ipsum has been the industry's standard dummy text ever since.</p>
  </section>

  <footer class="abs footer"></footer>
  <h4 class="abs footer-title" style="left:109px">Quick Link</h4>
  <h4 class="abs footer-title" style="left:197px">Testimonial</h4>
  <h4 class="abs footer-title" style="left:403px">Blog</h4>
  <h4 class="abs footer-title" style="left:573px">Address</h4>

  <ul class="abs quick-links">
    <li>Home</li><li>About us</li><li>Team</li><li>Career</li><li>Contact</li><li>Privacy Policy</li><li>FAQ</li>
  </ul>

  <div class="abs testimonial" style="top:1048px">
    <div class="avatar" role="img" aria-label="Client portrait"></div>
    <p class="footer-copy">Lorem Ipsum has been the industry's standard dummy text<i>- Mara Quell</i></p>
  </div>
  <div class="abs testimonial" style="top:1101px">
    <div class="avatar" role="img" aria-label="Client portrait"></div>
    <p class="footer-copy">Lorem Ipsum has been the industry's standard dummy text<i>- Mara Quell</i></p>
  </div>
  <div class="abs footer-arrows">
    <span><svg width="7" height="5" viewBox="0 0 7 5"><path d="M7 2.5H1M3 .5 1 2.5l2 2" fill="none" stroke="#fff" stroke-width=".9"/></svg></span>
    <span><svg width="7" height="5" viewBox="0 0 7 5"><path d="M0 2.5h6M4 .5l2 2-2 2" fill="none" stroke="#fff" stroke-width=".9"/></svg></span>
  </div>

  <p class="abs footer-copy blog-item" style="top:1047px">Lorem Ipsum has been the industry's standard dummy text<i style="margin-top:4px">- Mara Quell &nbsp;&nbsp; 15 Dec 2013</i></p>
  <p class="abs footer-copy blog-item" style="top:1098px">Lorem Ipsum has been the industry's standard dummy text<i style="margin-top:4px">- Mara Quell &nbsp;&nbsp; 15 Dec 2013</i></p>
  <span class="abs view-more">View More</span>

  <p class="abs footer-copy address">Lorem Ipsum has been the industry's standard dummy text</p>
  <div class="abs contact-line" style="top:1088px">
    <svg width="9" height="10" viewBox="0 0 9 10"><path d="M2 0 3.5 2.6 2.4 3.8c.7 1.6 1.7 2.7 3 3.4L6.6 6 9 7.6 8 9.6C4 9.5.5 5.8.3 1.2z" fill="#fff"/></svg>
    <span>1111 1111</span>
  </div>
  <div class="abs contact-line" style="top:1104px">
    <svg width="10" height="7" viewBox="0 0 10 7"><rect x=".5" y=".5" width="9" height="6" fill="none" stroke="#fff"/><path d="M.5.5 5 4 9.5.5" fill="none" stroke="#fff"/></svg>
    <span>hello@corvane.example</span>
  </div>
  <div class="abs social"><span></span><span></span><span></span><span></span></div>
</body>
</html>
```